Brightwater Charity Ball Poster

We are looking for a poster for our upcoming event, "Brightwater Charity Ball" - a sit down dinner formal event hosted by our university club, OKRU.
Usually we source designs internally from our committee (even if they aren't the most amazing quality), however this time round we have no one available to do it as everyone is a volunteer.
The event's theme is 'winter wonderland', based around the snowy forests you see in Veltmoor or Crown of Ashes (neither of these specific things are the theme however). Our venue is a clear-roof marque in a space surrounded by very tall pine trees giving off the forest vibe, and there are festoons strung between the trees so this is an element of warm light amongst the forest, perhaps a building or village tucked away in the forest.
The poster is for printing out at A3 size, and we will also need to create a Facebook event cover photo and other marketing graphics from the original poster files so some flexibility in the design and original files are required.
Things that need to be included on the poster :
---Event details
Brightwater Charity Ball
Saturday 12th August
7pm – midnight
Halberd Auditorium, KPC
Tables of 10
Members - $140
Non members - $150
All profits donated to Stride for Hope
---- Extra info and images (can be at the bottom, in corners etc,)
18+ ID required | Drink Responsibly
OKRU Logo
KPC Union Logo
(these logos may be changed to black and white if need be)
Example images of styles, colours and the sort of landscape we want for the poster can be found in the document attached.

```html
<!DOCTYPE html>
<html lang="en">
<head>
<meta charset="utf-8">
<title>Brightwater Charity Ball</title>
<link href="https://fonts.googleapis.com/css2?family=Chewy&family=Kurale&display=swap" rel="stylesheet">
<style>
  :root {
    --frost-white: #f2fbff;
    --frost-ice: #bfeaf7;
    --forest-violet: #6d58c9;
    --forest-indigo: #3f3fb8;
    --forest-cyan: #7fd3ee;
    --disc-blue: rgba(28, 48, 214, 0.86);
    --flake-tint: rgba(196, 204, 255, 0.85);
    --title-yellow: #fff23a;
    --title-gold: #ffd21a;
    --title-orange: #ff9418;
    --ink-white: #ffffff;
    --partner-ink: #ffffff;
  }
  html, body {
    margin: 0;
    padding: 0;
    width: 849px;
    height: 1200px;
    overflow: hidden;
    background: #ffffff;
  }
  .poster {
    position: relative;
    width: 849px;
    height: 1200px;
    overflow: hidden;
    font-family: "Kurale", Georgia, serif;
    color: var(--ink-white);
  }
  .forest-scene {
    position: absolute;
    inset: 0;
    background:
      linear-gradient(to bottom, var(--frost-white) 0%, rgba(220,244,252,0.85) 22%, rgba(191,234,247,0.35) 40%, rgba(191,234,247,0) 55%),
      linear-gradient(to bottom, rgba(255,255,255,0) 78%, rgba(236,230,255,0.9) 100%),
      radial-gradient(ellipse at 50% 78%, rgba(40,40,150,0.55) 0%, rgba(40,40,150,0) 55%),
      linear-gradient(95deg, var(--forest-violet) 0%, #7a6fd8 18%, #5a7fe0 45%, #6cc0ea 72%, var(--forest-cyan) 88%, #a9e6f4 100%);
  }
  .event-title {
    position: absolute;
    left: 0;
    right: 0;
    top: 168px;
    margin: 0;
    text-align: center;
    font-family: "Chewy", "Comic Sans MS", cursive;
    font-weight: 400;
    text-transform: uppercase;
    line-height: 1;
    filter: drop-shadow(3px 5px 3px rgba(30, 20, 70, 0.6));
  }
  .event-title span {
    display: block;
    background: linear-gradient(to bottom, var(--title-yellow) 0%, var(--title-gold) 55%, var(--title-orange) 100%);
    -webkit-background-clip: text;
    background-clip: text;
    color: transparent;
  }
  .title-line-one {
    font-size: 92px;
    transform: rotate(5deg) translateX(-4px);
  }
  .title-line-two {
    font-size: 82px;
    margin-top: -2px;
    transform: rotate(4deg) translateX(-12px);
  }
  .details-disc {
    position: absolute;
    left: 64px;
    top: 372px;
    width: 720px;
    height: 628px;
    border-radius: 50%;
    background: var(--disc-blue);
  }
  .snowflakes {
    position: absolute;
    inset: 0;
    width: 849px;
    height: 1200px;
    pointer-events: none;
  }
  .details {
    position: absolute;
    left: 0;
    right: 0;
    top: 452px;
    text-align: center;
    text-shadow: 1px 2px 3px rgba(10, 10, 60, 0.55);
  }
  .details p { margin: 0; }
  .event-date { font-size: 42px; line-height: 50px; }
  .event-time { font-size: 42px; line-height: 48px; }
  .event-venue { font-size: 36px; line-height: 48px; }
  .pricing { margin-top: 16px; }
  .pricing-heading {
    display: inline-block;
    font-size: 40px;
    line-height: 40px;
    border-bottom: 1.5px solid var(--ink-white);
  }
  .price-row { font-size: 40px; line-height: 42px; }
  .charity-note {
    margin-top: 22px !important;
    font-size: 38px;
    line-height: 38px;
    text-transform: uppercase;
  }
  .entry-note {
    margin-top: 26px !important;
    font-size: 31px;
    line-height: 36px;
  }
  .partners {
    position: absolute;
    left: 0;
    right: 0;
    top: 1078px;
    display: flex;
    justify-content: center;
    gap: 170px;
    align-items: center;
  }
  .partner {
    display: flex;
    align-items: center;
    gap: 10px;
    font-family: "Kurale", Georgia, serif;
    font-size: 32px;
    color: var(--partner-ink);
    text-shadow: none;
  }
  .partner-square {
    width: 22px;
    height: 22px;
    background: var(--partner-ink);
  }
  .partner-circle {
    width: 24px;
    height: 24px;
    border-radius: 50%;
    background: var(--partner-ink);
  }
</style>
</head>
<body>
  <main class="poster">
    <div class="forest-scene" role="img" aria-label="Photograph of a frosted winter forest: tall snow-covered tree trunks in violet and icy blue light, with snowflakes drifting across the treetops"></div>

    <h1 class="event-title">
      <span class="title-line-one">Brightwater</span>
      <span class="title-line-two">Charity Ball</span>
    </h1>

    <div class="details-disc"></div>

    <svg class="snowflakes" viewBox="0 0 849 1200" aria-hidden="true">
      <defs>
        <g id="flake-arm" stroke-linecap="round">
          <line x1="0" y1="0" x2="0" y2="-40" stroke-width="7"/>
          <polyline points="-11,-28 0,-17 11,-28" fill="none" stroke-width="6"/>
          <polyline points="-9,-40 0,-31 9,-40" fill="none" stroke-width="5"/>
        </g>
        <g id="snowflake" stroke="var(--flake-tint)">
          <use href="#flake-arm"/>
          <use href="#flake-arm" transform="rotate(60)"/>
          <use href="#flake-arm" transform="rotate(120)"/>
          <use href="#flake-arm" transform="rotate(180)"/>
          <use href="#flake-arm" transform="rotate(240)"/>
          <use href="#flake-arm" transform="rotate(300)"/>
        </g>
      </defs>
      <use href="#snowflake" transform="translate(164 676) scale(0.9)"/>
      <use href="#snowflake" transform="translate(690 690) scale(1.2)"/>
      <use href="#snowflake" transform="translate(725 609) scale(0.72)"/>
    </svg>

    <section class="details">
      <p class="event-date">Saturday 12th August</p>
      <p class="event-time">7pm – midnight</p>
      <p class="event-venue">Halberd Auditorium, KPC</p>

      <div class="pricing">
        <p class="pricing-heading">Tables of 10</p>
        <p class="price-row">Members - $140</p>
        <p class="price-row">Non members - $150</p>
      </div>

      <p class="charity-note">All profits donated to<br>Stride for Hope</p>

      <p class="entry-note">18+ ID required<br>Drink Responsibly</p>
    </section>

    <footer class="partners">
      <div class="partner"><span class="partner-square"></span>KPC Union</div>
      <div class="partner"><span class="partner-circle"></span>OKRU</div>
    </footer>
  </main>
</body>
</html>
```